Screendesign für neue Website
Alles zur vollsten Zufriedenheit abgelaufen.
Zielgruppe
Bauherren und alle die mal zum Architekten müssen.
Aufgabenstellung
Bei diesem Auftrag handelt es sich um die Erstellung eines Screendesigns für eine Website eines Archtiktenbüros.
Es wird daher ein Layout im PSD-Format erwartet, eine Umsetzung dessen in HTML wird nicht gefordert.

```html
<!DOCTYPE html>
<html lang="de">
<head>
<meta charset="utf-8">
<title>Georg Lindner Planungsunternehmen</title>
<link rel="stylesheet" href="https://fonts.googleapis.com/css2?family=Source+Sans+3:wght@400&family=Arimo:wght@400&display=swap">
<style>
:root{
  --stage:#c8c8c8;
  --white:#ffffff;
  --grey:#8c8c8c;
  --grey-band:rgba(150,150,150,.85);
  --green:#8ed13f;
  --ink:#111111;
}
*{box-sizing:border-box;margin:0;padding:0}
html,body{width:1200px;height:960px;overflow:hidden;background:var(--stage)}
.site{position:absolute;left:80px;top:134px;width:1036px;height:662px;background:var(--white);box-shadow:4px 5px 8px rgba(0,0,0,.35);overflow:hidden}
.header{position:absolute;left:0;top:0;width:1036px;height:147px;display:flex}
.photo{height:147px}
.band{position:absolute;left:0;top:105px;width:717px;height:42px;background:var(--grey-band)}
.rule{position:absolute;left:0;top:147px;width:717px;height:10px;background:var(--green)}
.rule-right{position:absolute;left:943px;top:147px;width:93px;height:10px;background:var(--green)}
.nav-column{position:absolute;left:717px;top:0;width:214px;height:662px;background:var(--grey);opacity:.95}
.nav-column-top{position:absolute;left:717px;top:0;width:214px;height:147px;background:linear-gradient(180deg,#9a9a96,#808080)}
.side-strip{position:absolute;left:931px;top:147px;width:12px;height:515px;background:var(--green)}
.nav{position:absolute;left:717px;top:213px;width:214px;list-style:none;border-bottom:6px solid var(--green)}
.nav li{height:59px;border-top:6px solid var(--green);font:21px/53px "Arimo",Arial,sans-serif;color:var(--ink);padding-left:28px;background:var(--grey)}
.claim{position:absolute;font:36px/1 "Source Sans 3","Myriad Pro",sans-serif;color:var(--ink);text-shadow:3px 4px 5px rgba(0,0,0,.45);white-space:nowrap}
.claim-1{left:94px;top:228px}
.claim-2{left:170px;top:307px}
.claim-3{left:250px;top:396px}
.claim-4{left:357px;top:486px}
.brand{position:absolute;left:12px;top:580px;display:flex;align-items:center;gap:28px}
.brand-mark{width:110px;height:66px;background:var(--ink)}
.brand-name{font:21px/26px "Arimo",Arial,sans-serif;color:var(--ink)}
</style>
</head>
<body>
<main class="site">
  <div class="header">
    <div class="photo" style="width:176px;background:linear-gradient(160deg,#1c3a66,#5fb9d8 55%,#204a6a)" role="img" aria-label="Beleuchteter Innenhof eines modernen Gebäudes bei Nacht"></div>
    <div class="photo" style="width:181px;background:linear-gradient(150deg,#0a0a2a,#c0379a 45%,#3a54c8 80%,#111)" role="img" aria-label="Farbig beleuchtete Glasfassade"></div>
    <div class="photo" style="width:192px;background:linear-gradient(150deg,#6d8fb8,#b06a35 45%,#7a4a26 80%,#445)" role="img" aria-label="Holzhaus mit Balkonen"></div>
    <div class="photo" style="width:168px;background:linear-gradient(160deg,#1f57b8,#e6e6e6 50%,#c7a53a 75%,#555)" role="img" aria-label="Weißes Wohnhaus mit Markisen vor blauem Himmel"></div>
    <div class="photo" style="width:214px"></div>
    <div class="photo" style="width:105px;background:linear-gradient(160deg,#0c2e7a,#6f8ec8 55%,#16246a)" role="img" aria-label="Geschwungene Glasfassade vor blauem Himmel"></div>
  </div>
  <div class="band"></div>
  <div class="nav-column"></div>
  <div class="nav-column-top" role="img" aria-label="Betonbau mit Treppe"></div>
  <div class="rule"></div>
  <div class="rule-right"></div>
  <div class="side-strip"></div>

  <p class="claim claim-1">Architekten schaffen</p>
  <p class="claim claim-2">Lebens-Raum</p>
  <p class="claim claim-3">Lebens-Traum</p>
  <p class="claim claim-4">Traum Haus</p>

  <ul class="nav">
    <li>Unternehmen</li>
    <li>Projekte</li>
    <li>Information</li>
    <li>Aktuelles</li>
    <li>Leistungen</li>
    <li>Kontakt</li>
  </ul>

  <div class="brand">
    <div class="brand-mark"></div>
    <p class="brand-name">Georg Lindner<br>Planungsunternehmen</p>
  </div>
</main>
</body>
</html>
```